弊社は、千葉の農産品などを原料にしたお酒や食品の開発・販売を行っております。
この度、南房総産レモンを100%使用したワインのリニューアルを予定しております。
それにあたってこれまでのラベルイメージを大幅に刷新したデザインを希望いたします。

イメージとしては、南房総の南国の気風を感じつつも、これまでよりも高級感のあるデザインで、ターゲットとしては30代、40代のややミドルエイジの女性をターゲットとしたものを希望します。

①ラベルサイズ・・・横×縦で、110㎜×120㎜ の大きさに限られます。
②-1ラベル記載事項・・・商品名、酒分類(この場合「甘味果実酒」)、『お酒(さけ)』のマークは必須(添付資料ご参照)。

文字pt(ポイント)は下記より大きいサイズでお願いします。
・お酒 24pt
・甘未果実酒 12pt

その他何かご不明な点がございましたら、お気軽にご質問下さい。
よろしくお願いいたします。

文字の視認性の良さと、南房総のイメージを想起させるイメージを持ちながら、女性にも親しみやすいデザインの良さというポイントで選ばせて頂きました。
当選者のラベルは、文字が色付きですが見やすく、またレモンの黄色と空の青い色の柔らかい配色のバランスが、シンプルですがわかりやすく綺麗で親しみを持てました。

今回の難しいテーマに、多くのデザイン案を頂戴し誠にありがとうございました。
今回の経験を、今後のPBの開発などにて活かしていきたいと存じます。

```html
<!DOCTYPE html>
<html lang="ja">
<head>
<meta charset="utf-8">
<title>南房総 レモンワイン ラベル</title>
<link rel="stylesheet" href="https://fonts.googleapis.com/css2?family=Noto+Serif+JP:wght@600;700;900&family=M+PLUS+Rounded+1c:wght@700;800&family=Playfair+Display:wght@700;900&display=swap">
<style>
  :root{
    --page:#ffffff;
    --ink:#1c1c22;
    --lemon:#f6e43a;
    --lemon-deep:#e7b81c;
    --wine:#e0335f;
    --wine-deep:#a51f3b;
    --gold:#e8c25a;
    --navy:#1d2840;
    --navy-deep:#121a2c;
    --violet:#8e7bb8;
    --accent-red:#e2334a;
    --white:#ffffff;
  }
  *{margin:0;padding:0;box-sizing:border-box}
  html,body{width:1200px;height:2616px;overflow:hidden;background:var(--page)}
  .sheet{position:relative;width:1200px;height:2616px}
  .label{position:absolute;left:0;width:1200px}
  .label svg.base{position:absolute;left:0;top:0}
  .t{position:absolute;white-space:nowrap;line-height:1}

  /* Label A : scalloped */
  .label-a{top:0;height:1220px}
  .a-origin{left:0;width:1200px;text-align:center;top:150px;font-family:"Noto Serif JP",serif;font-weight:700;font-size:54px;color:var(--ink);line-height:1.25;text-shadow:0 0 10px rgba(255,255,255,.8)}
  .a-region{left:220px;top:350px;padding:14px 26px;font-family:"Noto Serif JP",serif;font-weight:900;font-size:96px;color:var(--ink);
    background:linear-gradient(90deg,#5fe6ee,#b7e3f2 45%,#f2a0c8);border:4px solid var(--ink);border-radius:10px}
  .a-name{left:130px;top:505px;font-family:"Playfair Display",serif;font-weight:900;font-size:170px;letter-spacing:2px}
  .a-name .lemon{color:var(--lemon);-webkit-text-stroke:4px #4a3d0a;text-shadow:0 0 18px rgba(255,240,120,.9)}
  .a-name .wine{color:var(--wine);-webkit-text-stroke:3px var(--lemon);margin-left:24px;text-shadow:0 0 14px rgba(255,255,200,.8)}
  .a-class{left:700px;top:888px;width:340px;height:84px;display:flex;align-items:center;justify-content:center;
    font-family:"Noto Serif JP",serif;font-weight:700;font-size:56px;color:var(--gold);background:var(--wine-deep);border:4px solid var(--gold);border-radius:12px}
  .a-sake{left:330px;top:960px;width:140px;height:110px;display:flex;align-items:center;justify-content:center;
    font-family:"M PLUS Rounded 1c",sans-serif;font-weight:800;font-size:64px;color:var(--ink);
    background:radial-gradient(ellipse,var(--lemon) 55%,rgba(246,228,58,0) 72%)}

  /* Label B : navy disc */
  .label-b{top:1360px;height:1220px}
  .b-region{left:160px;top:455px;font-family:"Noto Serif JP",serif;font-weight:700;font-size:96px;color:var(--white)}
  .b-sake{left:700px;top:420px;width:260px;height:100px;text-align:center;font-family:"M PLUS Rounded 1c",sans-serif;font-weight:700;font-size:92px;color:var(--white)}
  .b-name{left:160px;top:600px;font-family:"Noto Serif JP",serif;font-weight:900;font-size:150px;color:var(--white);letter-spacing:6px}
  .b-name span{display:inline-block;padding-bottom:6px}
  .b-name .first{border-bottom:10px solid var(--accent-red)}
  .b-name .second{border-bottom:10px solid var(--lemon);text-shadow:0 0 16px rgba(226,51,74,.9)}
  .b-class{left:460px;top:820px;width:330px;height:96px;display:flex;align-items:center;justify-content:center;
    font-family:"Noto Serif JP",serif;font-weight:700;font-size:58px;color:var(--accent-red);border:4px solid var(--gold)}
  .b-origin{left:0;width:1200px;text-align:center;top:955px;font-family:"Noto Serif JP",serif;font-weight:700;font-size:64px;color:var(--white)}
  .b-origin em{font-style:normal;color:var(--accent-red)}
</style>
</head>
<body>
<main class="sheet">

  <section class="label label-a">
    <svg class="base" width="1200" height="1220" viewBox="0 0 1200 1220">
      <defs>
        <clipPath id="scallop">
          <circle cx="600" cy="610" r="470"/>
          <circle cx="1060" cy="610" r="85"/><circle cx="1025" cy="786" r="85"/>
          <circle cx="925.3" cy="935.3" r="85"/><circle cx="776" cy="1035" r="85"/>
          <circle cx="600" cy="1070" r="85"/><circle cx="424" cy="1035" r="85"/>
          <circle cx="274.7" cy="935.3" r="85"/><circle cx="175" cy="786" r="85"/>
          <circle cx="140" cy="610" r="85"/><circle cx="175" cy="434" r="85"/>
          <circle cx="274.7" cy="284.7" r="85"/><circle cx="424" cy="185" r="85"/>
          <circle cx="600" cy="150" r="85"/><circle cx="776" cy="185" r="85"/>
          <circle cx="925.3" cy="284.7" r="85"/><circle cx="1025" cy="434" r="85"/>
        </clipPath>
        <linearGradient id="sceneTone" x1="0" y1="0" x2="0" y2="1">
          <stop offset="0" stop-color="#e9e2ee"/>
          <stop offset=".35" stop-color="#d9c7d8"/>
          <stop offset=".55" stop-color="#c7cfe0"/>
          <stop offset=".75" stop-color="#e4dfe6"/>
          <stop offset="1" stop-color="#cfc2cf"/>
        </linearGradient>
      </defs>
      <rect role="img" aria-label="海を望む白いバルコニーとテーブルの写真" x="0" y="0" width="1200" height="1220" fill="url(#sceneTone)" clip-path="url(#scallop)"/>
      <rect role="img" aria-label="ヤシの木のイラスト" x="590" y="360" width="70" height="100" rx="8" fill="#2a2a2a" opacity=".85"/>
      <rect role="img" aria-label="ワインボトルとグラスのイラスト" x="700" y="380" width="70" height="110" rx="8" fill="#4a1622" opacity=".85"/>
    </svg>
    <p class="t a-origin">南房総産<br>レモン100%</p>
    <p class="t a-region">南房総</p>
    <p class="t a-name"><span class="lemon">Lemon</span><span class="wine">wine</span></p>
    <p class="t a-class">甘味果実酒</p>
    <p class="t a-sake">お酒</p>
  </section>

  <section class="label label-b">
    <svg class="base" width="1200" height="1220" viewBox="0 0 1200 1220">
      <defs>
        <radialGradient id="navyTone" cx=".45" cy=".45" r=".6">
          <stop offset="0" stop-color="#33405e"/>
          <stop offset=".7" stop-color="var(--navy)"/>
          <stop offset="1" stop-color="var(--navy-deep)"/>
        </radialGradient>
      </defs>
      <circle cx="600" cy="610" r="575" fill="url(#navyTone)"/>
      <ellipse role="img" aria-label="レモンと葉のイラスト" cx="360" cy="180" rx="150" ry="120" fill="#f0d640"/>
      <rect role="img" aria-label="ヤシの木のアイコン" x="470" y="440" width="60" height="90" rx="8" fill="#d8d8de" opacity=".6"/>
      <circle cx="780" cy="475" r="130" fill="var(--violet)" opacity=".55"/>
      <circle cx="880" cy="475" r="130" fill="var(--violet)" opacity=".45"/>
      <rect role="img" aria-label="シャンパンボトルのイラスト" x="820" y="810" width="100" height="120" rx="10" fill="#2b3a28" opacity=".9"/>
    </svg>
    <p class="t b-region">南房総</p>
    <p class="t b-sake">お酒</p>
    <p class="t b-name"><span class="first">レモン</span><span class="second">ワイン</span></p>
    <p class="t b-class">甘味果実酒</p>
    <p class="t b-origin">南房総産レモン<em>100%</em></p>
  </section>

</main>
</body>
</html>
```